Todo-list with focus on focus

We are writing todo app which is a to-do list/ outliner with focus support based on Steady method.

Attached are very rough mockups, but they are conceptually correct.

Main idea behind an app - minimum (unneeded) functionality and maximum benefit to the user.

So, everything must be very intuitive, fast, and without distractions (let's say Quince-style)

Target Market(s)

People who want to spend less time organizing their todo list than using it

Industry/Entity Type

It Support

Requirements
Must have
• Everything which is in mockups, maybe you can drop 1 or 2 if absolutely needed.
Nice to have
• 1. We would like to see such pallete here: http://www.huebinder.example/palette/482706/Mossy_Harbor_Dusk but it's not mandatory.
If you propose some other pallete, please make sure it's beautiful.

2. It would be good to somehow indicate that project is a goal in project list, and task is a goal in goal's list

3. Inbox should be accessible easliy, probably by sticking it to the top of Projects list somehow.

4. If you are able to propose another way to deal with such amount of options to deal with tasks other than radial menu - you are free to do it, if it'll work.

5. Priority, tags - very nice to have if they will fit into conception.

6. Maybe you can add other stuff we have overlooked.
But, if added, it must be very simple and needed.

```html
<!DOCTYPE html>
<html lang="en">
<head>
<meta charset="utf-8">
<title>Steady method – screens</title>
<link rel="stylesheet" href="https://fonts.googleapis.com/css2?family=Exo+2:wght@400;500;600;700&display=swap">
<style>
  :root {
    --teal: #6cc6ca;
    --teal-dark: #5bb8bc;
    --teal-line: #4fa9ad;
    --teal-text: #5cc0c5;
    --white: #ffffff;
    --paper: #f3f3f3;
    --tab-bg: #f4f4f4;
    --status: #1e1e1e;
    --danger: #c81e26;
    --key: #fdfdfd;
    --key-dark: #a9b0ba;
    --kb-bg: #d2d5db;
    --go: #2f7ae5;
    --ink: #2a2a2a;
    --canvas: #ffffff;
  }
  * { box-sizing: border-box; margin: 0; padding: 0; }
  html, body { width: 1200px; height: 1000px; overflow: hidden; background: var(--canvas); }
  body { position: relative; font-family: "Exo 2", sans-serif; }

  .screen { position: absolute; width: 158px; height: 238px; overflow: hidden; background: var(--white); display: flex; flex-direction: column; }
  .s-splash   { left: 98px;  top: 131px; }
  .s-list     { left: 379px; top: 131px; }
  .s-new      { left: 655px; top: 131px; }
  .s-focus    { left: 927px; top: 131px; }
  .s-break    { left: 98px;  top: 618px; }
  .s-history  { left: 384px; top: 618px; }
  .s-goals    { left: 657px; top: 618px; }
  .s-settings { left: 927px; top: 618px; }

  .status-bar { height: 9px; background: var(--status); color: var(--white); font: 600 6px/9px "Exo 2", sans-serif; display: flex; justify-content: space-between; padding: 0 4px; flex: none; }
  .status-bar .battery { width: 10px; height: 5px; border: 1px solid var(--white); margin-top: 2px; }

  .tab-bar { height: 18px; background: var(--tab-bg); display: flex; flex: none; margin-top: auto; }
  .tab-bar .tab { flex: 1; display: flex; align-items: center; justify-content: center; border-left: 1px solid #d8d8d8; }
  .tab-bar .tab:first-child { border-left: none; }
  .tab-bar svg { width: 11px; height: 11px; fill: var(--teal-text); }

  .row { height: 31px; background: var(--teal); border-bottom: 1px solid var(--teal-line); color: var(--white); font-weight: 600; font-size: 11px; display: flex; align-items: center; justify-content: space-between; padding: 0 6px; flex: none; }
  .row .grip { width: 9px; height: 5px; border-top: 1px solid #8fd4d7; border-bottom: 1px solid #8fd4d7; position: relative; }
  .row .grip::after { content: ""; position: absolute; left: 0; right: 0; top: 1px; border-top: 1px solid #8fd4d7; }
  .row .date { font-size: 6px; font-weight: 500; }

  /* splash */
  .s-splash { align-items: center; justify-content: center; }
  .splash-mark { width: 40px; height: 46px; border: 3px solid var(--teal-text); }
  .splash-title { color: var(--teal-text); font-weight: 600; font-size: 11px; line-height: 14px; text-align: center; margin-top: 12px; }

  /* task list */
  .task-header { height: 53px; background: var(--teal-dark); color: var(--white); display: flex; justify-content: space-between; align-items: center; padding: 0 6px; border-bottom: 1px solid var(--teal-line); flex: none; }
  .task-header .name { font-size: 17px; font-weight: 500; line-height: 18px; }
  .task-header .time { font-size: 23px; font-weight: 700; }
  .row.swiped { padding: 0; justify-content: flex-end; }
  .row.swiped .chev { color: #9fdadd; font-size: 14px; margin-right: 6px; }
  .row.swiped .delete { background: var(--danger); height: 100%; width: 53px; display: flex; align-items: center; justify-content: center; }

  /* new task */
  .new-form { background: var(--teal); height: 122px; padding: 6px 7px; color: var(--white); flex: none; }
  .new-form h1 { font-size: 16px; font-weight: 500; line-height: 18px; margin-bottom: 2px; }
  .new-form label { display: block; font-size: 7px; line-height: 8px; margin-top: 3px; }
  .new-form .field { background: var(--white); color: var(--teal-text); font-size: 10px; font-weight: 600; height: 13px; line-height: 13px; padding: 0 3px; }
  .new-form .field.wide { width: 136px; }
  .new-form .field.short { display: inline-block; }
  .keyboard { background: var(--kb-bg); flex: 1; padding: 4px 2px; display: flex; flex-direction: column; gap: 4px; }
  .kb-row { display: flex; gap: 2px; justify-content: center; }
  .key { width: 13.5px; height: 20px; background: var(--key); border-radius: 3px; font: 500 9px/20px Arial, sans-serif; text-align: center; color: var(--ink); box-shadow: 0 1px 0 #8a8f96; }
  .key.mod { background: var(--key-dark); color: var(--white); width: 18px; font-size: 7px; }
  .key.wide { width: 26px; font-size: 7px; }
  .key.go { background: var(--go); color: var(--white); width: 36px; font-size: 8px; }

  /* focus */
  .s-focus { background: var(--paper); align-items: center; color: var(--teal-text); }
  .focus-name { font-size: 28px; font-weight: 400; line-height: 34px; text-align: center; margin-top: 26px; }
  .focus-time { font-size: 34px; font-weight: 700; line-height: 40px; margin-top: 2px; }
  .focus-actions { display: flex; gap: 16px; margin-top: 10px; }
  .ring { width: 50px; height: 50px; border-radius: 50%; border: 2px solid var(--teal-text); display: flex; align-items: center; justify-content: center; font-weight: 600; }
  .ring.big { font-size: 16px; }
  .ring.small { font-size: 7px; }

  /* break */
  .s-break { background: var(--teal); color: var(--white); align-items: center; }
  .break-title { font-size: 33px; font-weight: 700; margin-top: 58px; line-height: 44px; }
  .break-time { font-size: 33px; font-weight: 700; line-height: 44px; }
  .s-break .ring { border-color: var(--white); color: var(--white); font-size: 8px; font-weight: 500; margin-top: 16px; }

  /* headed lists */
  .page-title { height: 22px; background: var(--white); color: var(--teal-text); font-size: 16px; font-weight: 500; text-align: center; line-height: 22px; flex: none; border-bottom: 1px solid var(--teal-line); }
  .section { height: 13px; background: var(--white); color: var(--teal-text); font-size: 10px; line-height: 13px; padding: 0 5px; flex: none; }
  .s-history, .s-goals, .s-settings { background: var(--teal); }
  .s-goals .row, .s-settings .row { height: 30px; }
  .check { width: 10px; height: 10px; border: 1px solid var(--white); }
  .check svg { width: 10px; height: 10px; display: block; margin: -2px 0 0 1px; stroke: var(--white); fill: none; stroke-width: 2; }
</style>
</head>
<body>

<svg width="0" height="0" style="position:absolute" aria-hidden="true">
  <symbol id="i-flag" viewBox="0 0 12 12"><path d="M2 1h1v10H2zM3 1h7l-2 2.5L10 6H3z"/></symbol>
  <symbol id="i-history" viewBox="0 0 12 12"><path d="M6 1a5 5 0 1 1-4.6 3H0l2-2.5L4 4H2.6A3.8 3.8 0 1 0 6 2.2zM5.4 3.5h1.2v2.3l1.6 1.2-.7.9-2.1-1.5z"/></symbol>
  <symbol id="i-gear" viewBox="0 0 12 12"><path d="M5 0h2l.3 1.6 1.2.6 1.4-.9 1.4 1.4-.9 1.4.6 1.2L12 5v2l-1.6.3-.6 1.2.9 1.4-1.4 1.4-1.4-.9-1.2.6L7 12H5l-.3-1.6-1.2-.6-1.4.9-1.4-1.4.9-1.4-.6-1.2L0 7V5l1.6-.3.6-1.2-.9-1.4 1.4-1.4 1.4.9 1.2-.6zM6 4a2 2 0 1 0 0 4 2 2 0 0 0 0-4z"/></symbol>
</svg>

<!-- Splash -->
<section class="screen s-splash">
  <span class="splash-mark" aria-hidden="true"></span>
  <p class="splash-title">Steady<br>method</p>
</section>

<!-- Task list -->
<section class="screen s-list">
  <div class="status-bar"><span>Norcell</span><span>12:34 PM</span><span class="battery"></span></div>
  <header class="task-header"><span class="name">App<br>design</span><span class="time">24:19</span></header>
  <div class="row"><span>Music</span><span class="grip"></span></div>
  <div class="row"><span>Research</span><span class="grip"></span></div>
  <div class="row swiped"><span class="chev">&laquo;</span><span class="delete">Delete</span></div>
  <div class="row"><span>Bank</span><span class="grip"></span></div>
  <div class="row"><span>Blog</span><span class="grip"></span></div>
  <nav class="tab-bar">
    <span class="tab"><svg><use href="#i-flag"/></svg></span>
    <span class="tab"><svg><use href="#i-history"/></svg></span>
    <span class="tab"><svg><use href="#i-gear"/></svg></span>
  </nav>
</section>

<!-- New task -->
<section class="screen s-new">
  <div class="status-bar"><span>Norcell</span><span>12:34 PM</span><span class="battery"></span></div>
  <form class="new-form">
    <h1>New task</h1>
    <label>Task name</label>
    <div class="field wide">App design</div>
    <label>Time left</label>
    <div class="field short">25:00</div>
    <label>Date</label>
    <div class="field short">15/02/2013</div>
  </form>
  <div class="keyboard">
    <div class="kb-row"><span class="key">Q</span><span class="key">W</span><span class="key">E</span><span class="key">R</span><span class="key">T</span><span class="key">Y</span><span class="key">U</span><span class="key">I</span><span class="key">O</span><span class="key">P</span></div>
    <div class="kb-row"><span class="key">A</span><span class="key">S</span><span class="key">D</span><span class="key">F</span><span class="key">G</span><span class="key">H</span><span class="key">J</span><span class="key">K</span><span class="key">L</span></div>
    <div class="kb-row"><span class="key mod">&#8679;</span><span class="key">Z</span><span class="key">X</span><span class="key">C</span><span class="key">V</span><span class="key">B</span><span class="key">N</span><span class="key">M</span><span class="key mod">&#9003;</span></div>
    <div class="kb-row"><span class="key mod wide">@123</span><span class="key">.</span><span class="key">/</span><span class="key wide">.com</span><span class="key go">Go</span></div>
  </div>
</section>

<!-- Focus timer -->
<section class="screen s-focus">
  <p class="focus-name">App<br>design</p>
  <p class="focus-time">22:34</p>
  <div class="focus-actions">
    <span class="ring big">Stop</span>
    <span class="ring small">Complete</span>
  </div>
</section>

<!-- Break -->
<section class="screen s-break">
  <p class="break-title">Break</p>
  <p class="break-time">03:12</p>
  <span class="ring">Complete</span>
</section>

<!-- History -->
<section class="screen s-history">
  <div class="status-bar"><span>Norcell</span><span>12:34 PM</span><span class="battery"></span></div>
  <h2 class="page-title">History</h2>
  <div class="row"><span>App Design</span><span class="date">15/02/2013</span></div>
  <div class="row"><span>Music</span><span class="date">14/01/2013</span></div>
  <div class="row"><span>Research</span><span class="date">13/01/2013</span></div>
  <div class="row"><span>Lunch</span><span class="date">13/01/2013</span></div>
  <div class="row"><span>Bank</span><span class="date">12/01/2013</span></div>
  <div class="row"><span>Blog</span><span class="date">11/01/2013</span></div>
  <nav class="tab-bar">
    <span class="tab"><svg><use href="#i-flag"/></svg></span>
    <span class="tab"><svg><use href="#i-history"/></svg></span>
    <span class="tab"><svg><use href="#i-gear"/></svg></span>
  </nav>
</section>

<!-- Goals -->
<section class="screen s-goals">
  <div class="status-bar"><span>Norcell</span><span>12:34 PM</span><span class="battery"></span></div>
  <h2 class="page-title">Goals</h2>
  <div class="section">Daily goals</div>
  <div class="row"><span>Research</span></div>
  <div class="row"><span>Bank</span></div>
  <div class="section">Weekly goals</div>
  <div class="row"><span>App Design</span></div>
  <div class="section">Monthly goals</div>
  <div class="row"><span>Music</span></div>
  <div class="row"><span>Blog</span></div>
  <nav class="tab-bar">
    <span class="tab"><svg><use href="#i-flag"/></svg></span>
    <span class="tab"><svg><use href="#i-history"/></svg></span>
    <span class="tab"><svg><use href="#i-gear"/></svg></span>
  </nav>
</section>

<!-- Settings -->
<section class="screen s-settings">
  <div class="status-bar"><span>Norcell</span><span>12:34 PM</span><span class="battery"></span></div>
  <h2 class="page-title">Settings</h2>
  <div class="section">Alert</div>
  <div class="row"><span>Sound</span><span class="check"><svg viewBox="0 0 10 10"><path d="M1 5l3 3 6-8"/></svg></span></div>
  <div class="row"><span>Vibration</span><span class="check"></span></div>
  <div class="section">Updates</div>
  <div class="row"><span>Automatically</span><span class="check"></span></div>
  <nav class="tab-bar">
    <span class="tab"><svg><use href="#i-flag"/></svg></span>
    <span class="tab"><svg><use href="#i-history"/></svg></span>
    <span class="tab"><svg><use href="#i-gear"/></svg></span>
  </nav>
</section>

</body>
</html>
```